Little Meadow Press Website

We need a wordpress design for a new independent children's book publishers based in Oxford in the UK. The design should be fun and colourful. I have supplied an example template of some of the text/images but open to other ideas.
The design should communicate that Little Meadow Press are producers of fun and interactive children's illustrated books.

Target Market(s)

Booksellers, International

```html
<!DOCTYPE html>
<html lang="en">
<head>
<meta charset="utf-8">
<title>Little Meadow Press</title>
<link rel="stylesheet" href="https://fonts.googleapis.com/css2?family=Roboto:ital,wght@0,300;0,400;0,500;1,400&family=Ubuntu:wght@400;500&display=swap">
<style>
:root{
  --sky-top:#c9ecfb;
  --sky-bottom:#ffffff;
  --navy:#2e3192;
  --lime:#8dc63f;
  --red:#ed1c24;
  --purple:#92278f;
  --cyan:#27aae1;
  --title-blue:#0b72b9;
  --hero-purple:#6a2a96;
  --text:#555;
  --orange:#f7941d;
  --yellow:#fff55f;
  --yellow-edge:#f7c21d;
  --panel:#f2f2f2;
  --date-red:#d8232a;
  --link-navy:#2e3192;
  --footer:#27aae1;
  --white:#fff;
}
*{box-sizing:border-box;margin:0;padding:0}
html,body{width:1200px;height:980px;overflow:hidden}
body{
  position:relative;
  font-family:"Roboto",Arial,sans-serif;
  color:var(--text);
  background:linear-gradient(to bottom,var(--sky-top) 0,#e6f6fd 300px,var(--sky-bottom) 500px);
}
.brand{position:absolute;left:75px;top:40px;display:flex;align-items:center;gap:10px}
.brand-dot{width:30px;height:30px;border-radius:50%;background:var(--cyan)}
.brand-name{font-family:"Ubuntu",sans-serif;font-size:20px;font-weight:500;color:var(--title-blue)}
.main-nav{position:absolute;left:317px;top:19px;display:flex;gap:5px}
.main-nav a{
  width:158px;height:84px;display:flex;align-items:center;justify-content:center;
  text-align:center;color:var(--white);text-decoration:none;font-size:13px;line-height:18px;text-transform:uppercase;
}
.nav-home{background:var(--navy)}
.nav-about{background:var(--lime)}
.nav-book{background:var(--red)}
.nav-authors{background:var(--purple)}
.nav-contact{background:var(--cyan)}
.hero{position:absolute;left:75px;top:109px;width:1051px;height:373px;background:var(--white);padding:4px}
.hero-photo{
  position:relative;width:100%;height:100%;
  background:linear-gradient(100deg,#efe6da 0%,#e8d2bb 35%,#d9b99a 55%,#f1e6dc 75%,#c8d98a 100%);
}
.hero-title{
  position:absolute;left:28px;top:124px;
  font-size:57px;line-height:61px;font-weight:400;color:var(--hero-purple);
}
.slider-dots{position:absolute;right:18px;bottom:14px;display:flex;gap:8px}
.slider-dots span{
  width:24px;height:24px;border-radius:50%;background:#222;color:var(--white);
  font-size:13px;font-weight:500;display:flex;align-items:center;justify-content:center;
}
.slider-dots .active{background:var(--cyan)}
.welcome{position:absolute;left:75px;top:520px;width:603px}
.section-title{font-family:"Ubuntu",sans-serif;font-weight:400;font-size:22px;color:var(--title-blue)}
.welcome p{margin-top:10px;font-size:13.5px;line-height:23px;font-weight:300;color:#444}
.btn-read{
  display:inline-block;margin-top:22px;background:var(--orange);color:var(--white);
  font-size:13px;padding:0 18px;height:38px;line-height:38px;text-decoration:none;text-transform:uppercase;
}
.aim{position:absolute;left:75px;top:727px;width:603px;height:122px;background:var(--yellow);border:3px double var(--yellow-edge);outline:1px solid var(--yellow-edge);outline-offset:-6px;padding:16px 18px}
.aim p{margin-top:8px;font-style:italic;font-size:14.5px;line-height:23px;color:#222}
.panel{position:absolute;left:704px;width:422px;background:var(--panel);padding:14px 22px}
.panel-news{top:523px;height:160px}
.panel-tweets{top:692px;height:159px}
.panel-head{display:flex;justify-content:space-between;align-items:center}
.panel-arrows{display:flex;gap:10px}
.panel-arrows svg{width:14px;height:16px}
.news-date{margin-top:10px;color:var(--date-red);font-size:13.5px;font-weight:500}
.panel p{margin-top:4px;font-size:13.5px;line-height:23px;font-weight:300;color:#444}
.panel-tweets p{margin-top:8px}
.panel-link{display:inline-block;margin-top:6px;color:var(--link-navy);font-size:13px;text-decoration:none;text-transform:uppercase}
.tweet-link{color:var(--date-red)}
.tweet-meta{margin-top:6px;font-size:13px;color:var(--link-navy)}
.site-footer{position:absolute;left:0;top:880px;width:1200px;height:100px;background:var(--footer);color:var(--white);font-size:13px;font-weight:300}
.footer-legal{position:absolute;left:74px;top:30px;line-height:24px}
.social{position:absolute;right:74px;top:37px;display:flex;gap:6px}
.social span{width:30px;height:30px;border-radius:50%;background:var(--white)}
</style>
</head>
<body>
<header>
  <div class="brand"><span class="brand-dot"></span><span class="brand-name">Little Meadow Press</span></div>
  <nav class="main-nav">
    <a class="nav-home" href="#">Home</a>
    <a class="nav-about" href="#">About</a>
    <a class="nav-book" href="#">Book</a>
    <a class="nav-authors" href="#">Authors /<br>Illustrators</a>
    <a class="nav-contact" href="#">Contact Us</a>
  </nav>
</header>

<section class="hero">
  <div class="hero-photo" role="img" aria-label="Photo of two young children lying on the floor reading a book, with a stack of colourful books beside them">
    <h1 class="hero-title">Bright Book for<br>Bright Minds..</h1>
    <div class="slider-dots"><span class="active">1</span><span>2</span><span>3</span></div>
  </div>
</section>

<section class="welcome">
  <h2 class="section-title">Welcome to Our Website</h2>
  <p>Little Meadow Press is a new independent publishing company publishing inspiring and quality children's illustrated books. Our aim is to print stories that are not only entertaining, but encourage and inspire children to explore different activities and aspects of life, as shown by our first two titles 'The Otter Tea Party' and 'Captain Poppy'</p>
  <a class="btn-read" href="#">Read More</a>
</section>

<section class="aim">
  <h2 class="section-title">Our Aim</h2>
  <p>“ Our books are aimed at one to five year olds and we are looking for new talent as well as established authors and illustrators...”</p>
</section>

<aside class="panel panel-news">
  <div class="panel-head">
    <h2 class="section-title">In the News</h2>
    <div class="panel-arrows">
      <svg viewBox="0 0 14 16"><path d="M10 2 4 8l6 6" fill="none" stroke="#333" stroke-width="1.6"/></svg>
      <svg viewBox="0 0 14 16"><path d="M4 2l6 6-6 6" fill="none" stroke="#333" stroke-width="1.6"/></svg>
    </div>
  </div>
  <div class="news-date">Mar 24, 2015</div>
  <p>Lorem ipsum dolor sit amet, consect- etuer adipiscing elit, sed diam nonummy nibh. Euismod tincidunt ut laoreet...</p>
  <a class="panel-link" href="#">Read More</a>
</aside>

<aside class="panel panel-tweets">
  <div class="panel-head">
    <h2 class="section-title">Latest Tweets</h2>
    <div class="panel-arrows">
      <svg viewBox="0 0 14 16"><path d="M10 2 4 8l6 6" fill="none" stroke="#333" stroke-width="1.6"/></svg>
      <svg viewBox="0 0 14 16"><path d="M4 2l6 6-6 6" fill="none" stroke="#333" stroke-width="1.6"/></svg>
    </div>
  </div>
  <p>Lorem ipsum dolor sit amet, consect- etuer adipiscing elit, sed diam nonummy nib <span class="tweet-link">hhttp://@lmpnews.com</span> Euismod tincidunt ut laoreet...</p>
  <div class="tweet-meta">3days ago &nbsp;|&nbsp; Retweets</div>
</aside>

<footer class="site-footer">
  <div class="footer-legal">Copyright ©2015.CompanyName.All Right Reserved<br>Privacy Policy &nbsp;|&nbsp; Site Map</div>
  <div class="social" aria-label="Social links"><span></span><span></span><span></span><span></span><span></span></div>
</footer>
</body>
</html>
```